Pebble Lane real estate investment company needs a poster design

We would like a poster design size 18 x 24.
Poster wording -
I WANT TO BUY YOUR ( finish with logo) logo uploaded
website- www.pebblelane-homes.example
phone # 555-217-8843 ( color red for the phone number)
we would like to see the poster on 2 different backgrounds
Yellow background
White background
horizontal

```html
<!DOCTYPE html>
<html lang="en">
<head>
<meta charset="utf-8">
<title>Pebble Lane – I Want To Buy Your House</title>
<link rel="stylesheet" href="https://fonts.googleapis.com/css2?family=Anton&family=Montserrat:wght@600;800&display=swap">
<style>
  :root {
    --ink: #000000;
    --sun: #fde35a;
    --sun-deep: #f2d548;
    --alert-red: #e8202d;
  }
  html, body {
    margin: 0;
    padding: 0;
    width: 900px;
    height: 1200px;
    overflow: hidden;
    background: var(--sun);
  }
  .poster {
    position: relative;
    width: 900px;
    height: 1200px;
    overflow: hidden;
    background: radial-gradient(circle at 50% 52%, var(--sun) 0%, var(--sun) 55%, var(--sun-deep) 100%);
  }
  .web-band {
    position: absolute;
    left: 0; top: 0;
    width: 900px;
    height: 114px;
    background: var(--ink);
    display: flex;
    align-items: center;
    justify-content: center;
  }
  .web-address {
    font-family: "Montserrat", sans-serif;
    font-weight: 600;
    font-size: 38px;
    letter-spacing: 0.12em;
    color: var(--sun);
    white-space: nowrap;
  }
  .headline {
    position: absolute;
    left: 0;
    top: 232px;
    width: 900px;
    margin: 0;
    text-align: center;
    font-family: "Anton", sans-serif;
    font-weight: 400;
    font-size: 142px;
    line-height: 130px;
    color: var(--ink);
    text-transform: uppercase;
  }
  .brand-name {
    position: absolute;
    left: 0;
    top: 680px;
    width: 900px;
    text-align: center;
    font-family: "Anton", sans-serif;
    font-weight: 400;
    font-size: 118px;
    line-height: 160px;
    color: var(--ink);
    text-transform: uppercase;
    white-space: nowrap;
  }
  .phone-band {
    position: absolute;
    left: 0; bottom: 0;
    width: 900px;
    height: 114px;
    background: var(--ink);
    display: flex;
    align-items: center;
    justify-content: center;
    gap: 22px;
  }
  .phone-icon { width: 74px; height: 74px; display: block; }
  .phone-number {
    font-family: "Montserrat", sans-serif;
    font-weight: 800;
    font-size: 72px;
    letter-spacing: 0.2em;
    color: var(--alert-red);
    white-space: nowrap;
  }
</style>
</head>
<body>
  <main class="poster">
    <header class="web-band">
      <span class="web-address">www.pebblelane-homes.example</span>
    </header>

    <h1 class="headline">I Want<br>To Buy<br>Your</h1>

    <div class="brand-name">Pebble Lane</div>

    <footer class="phone-band">
      <svg class="phone-icon" viewBox="0 0 74 74" aria-hidden="true">
        <circle cx="37" cy="37" r="33" fill="none" stroke="var(--alert-red)" stroke-width="5"/>
        <path d="M25 19c2-1 4-1 5 1l4 8c1 2 0 3-1 4l-3 3c2 5 6 9 11 11l3-3c1-1 3-2 4-1l8 4c2 1 2 3 1 5l-2 4c-2 3-6 4-10 2-12-5-20-13-24-25-1-4 0-8 4-13z" fill="var(--alert-red)"/>
      </svg>
      <span class="phone-number">555-217-8843</span>
    </footer>
  </main>
</body>
</html>
```